High-end residential home builder needs a business card design

We need a new business card design for a small residential construction company based in Boise, Idaho. We specialize in building custom high-end homes and remodels, with a focus on great design and craftsmanship.

We would like to use our current logo, but open to new color suggestions.
Just looking for a clean, sharp, modern design that looks high-end.

Target Market(s)

Upscale clientele

Industry/Entity Type

Contractor

Contact Information for Business Card

Company: Stonefield Custom Builders
Name: Marcus Tilley
Phone number: 208 367 4120
Email: MarcusTilleySCB@mailbox-example.com
Website: Stonefieldcustombuilders-example.com

Font styles to use
Serif
Sans Serif

Requirements
Must have
• Company Logo
Company name
My name
My phone number
My email
Company website
Nice to have
• I have attached a few photos of cards that I really like.

```html
<!DOCTYPE html>
<html lang="en">
<head>
<meta charset="utf-8">
<title>Stonefield Custom Builders – Business Card</title>
<link rel="stylesheet" href="https://fonts.googleapis.com/css2?family=Montserrat:wght@500;600;700&family=Poppins:wght@400;500;600&display=swap">
<style>
  :root {
    --stage: #262626;
    --card-white: #ffffff;
    --card-black: #0c0c0c;
    --ink: #1f1a17;
    --ink-soft: #2b2522;
    --accent: #e08a2c;
    --line: #3a302a;
    --white: #ffffff;
  }
  * { box-sizing: border-box; margin: 0; padding: 0; }
  html, body { width: 1200px; height: 900px; overflow: hidden; }
  body {
    background: var(--stage);
    display: flex;
    flex-direction: column;
    align-items: center;
    justify-content: center;
    gap: 56px;
    font-family: "Poppins", sans-serif;
  }
  .card {
    width: 640px;
    height: 366px;
    position: relative;
    box-shadow: 0 18px 40px rgba(0,0,0,0.45);
  }
  .card--front { background: var(--card-white); display: flex; align-items: center; }
  .card--back { background: var(--card-black); display: flex; align-items: center; justify-content: center; }

  .brand { display: flex; flex-direction: column; align-items: center; gap: 14px; }
  .brand__square { width: 22px; height: 22px; background: var(--ink); }
  .brand__name {
    font-family: "Montserrat", sans-serif;
    font-weight: 600;
    color: var(--ink);
    text-transform: uppercase;
    letter-spacing: 0.3em;
    text-align: center;
    line-height: 1.7;
    font-size: 17px;
  }
  .card--back .brand__square { background: var(--white); width: 26px; height: 26px; }
  .card--back .brand__name { color: var(--white); font-size: 20px; }

  .card__brand-side { width: 52%; display: flex; justify-content: center; }
  .card__divider { width: 1px; height: 190px; background: var(--line); }
  .card__contact-side { flex: 1; padding-left: 34px; }

  .person__name {
    font-family: "Montserrat", sans-serif;
    font-weight: 700;
    font-size: 19px;
    color: var(--ink);
    text-transform: uppercase;
    letter-spacing: 0.02em;
  }
  .person__role {
    font-size: 12.5px;
    font-weight: 500;
    color: var(--accent);
    text-transform: uppercase;
    letter-spacing: 0.04em;
    margin-bottom: 16px;
  }
  .contact-list { list-style: none; display: flex; flex-direction: column; gap: 8px; }
  .contact-list li {
    display: flex; align-items: center; gap: 8px;
    font-size: 11px; color: var(--ink-soft);
  }
  .contact-list svg { width: 13px; height: 13px; flex: none; }
</style>
</head>
<body>
  <section class="card card--front">
    <div class="card__brand-side">
      <div class="brand">
        <span class="brand__square"></span>
        <p class="brand__name">Stonefield<br>Custom Builders</p>
      </div>
    </div>
    <div class="card__divider"></div>
    <div class="card__contact-side">
      <h1 class="person__name">Marcus Tilley</h1>
      <p class="person__role">Managing Director</p>
      <ul class="contact-list">
        <li>
          <svg viewBox="0 0 24 24" aria-hidden="true"><path fill="var(--accent)" d="M6.6 10.8a15.1 15.1 0 0 0 6.6 6.6l2.2-2.2a1 1 0 0 1 1-.25 11.4 11.4 0 0 0 3.6.57 1 1 0 0 1 1 1V20a1 1 0 0 1-1 1A17 17 0 0 1 3 4a1 1 0 0 1 1-1h3.5a1 1 0 0 1 1 1c0 1.25.2 2.45.57 3.57a1 1 0 0 1-.25 1z"/></svg>
          208 367 4120
        </li>
        <li>
          <svg viewBox="0 0 24 24" aria-hidden="true"><rect x="2" y="5" width="20" height="14" fill="var(--accent)"/><path d="M2 5l10 8 10-8" fill="none" stroke="#fff" stroke-width="1.6"/></svg>
          MarcusTilleySCB@mailbox-example.com
        </li>
        <li>
          <svg viewBox="0 0 24 24" aria-hidden="true"><g fill="none" stroke="var(--accent)" stroke-width="1.8"><circle cx="12" cy="12" r="9"/><ellipse cx="12" cy="12" rx="4" ry="9"/><path d="M3 12h18M5 7h14M5 17h14"/></g></svg>
          Stonefieldcustombuilders-example.com
        </li>
      </ul>
    </div>
  </section>

  <section class="card card--back">
    <div class="brand">
      <span class="brand__square"></span>
      <p class="brand__name">Stonefield<br>Custom Builders</p>
    </div>
  </section>
</body>
</html>
```